Business Consulting Business Card

professional business card with basic information (1) First and Last name (2) email address, (3) phone number, (4) website.

```html
<!DOCTYPE html>
<html lang="en">
<head>
<meta charset="utf-8">
<title>Tide Harbor Business Card</title>
<link href="https://fonts.googleapis.com/css2?family=Montserrat:wght@400;500;600&display=swap" rel="stylesheet">
<style>
  :root {
    --backdrop: #1e1f21;
    --navy: #0b2b40;
    --teal: #4fc3c1;
    --sky: #45a9cf;
    --white: #ffffff;
    --ink: #1f3f55;
  }
  * { margin: 0; padding: 0; box-sizing: border-box; }
  html, body {
    width: 1200px; height: 900px; overflow: hidden;
    background: var(--backdrop);
    font-family: "Montserrat", sans-serif;
  }
  .canvas {
    position: relative; width: 1200px; height: 900px;
    display: flex; flex-direction: column; align-items: center; justify-content: center; gap: 46px;
  }
  .card {
    position: relative; width: 660px; height: 377px; overflow: hidden;
    box-shadow: 0 14px 30px rgba(0,0,0,.45);
  }
  /* front */
  .card--front {
    background: var(--navy);
    display: flex; flex-direction: column; align-items: center; justify-content: center; gap: 22px;
  }
  .brand-dot {
    width: 58px; height: 58px; border-radius: 50%;
    background: var(--teal);
  }
  .brand-name {
    color: var(--white); font-weight: 500; font-size: 30px; letter-spacing: 7px;
  }
  /* back */
  .card--back { background: var(--white); }
  .side-band {
    position: absolute; left: 0; top: 0; bottom: 0; width: 260px;
    background: var(--navy);
  }
  .side-band .brand-vertical {
    position: absolute; left: 148px; bottom: 112px;
    writing-mode: vertical-rl; transform: rotate(180deg);
    color: var(--white); font-weight: 500; font-size: 24px; letter-spacing: 5px; line-height: 1;
    white-space: nowrap;
  }
  .side-band .brand-dot {
    position: absolute; left: 132px; bottom: 38px; width: 56px; height: 56px;
  }
  .accent-stripe {
    position: absolute; top: 0; bottom: 0; left: 282px; width: 12px;
    background: var(--teal);
  }
  .contact {
    position: absolute; left: 372px; top: 132px; color: var(--ink);
  }
  .contact__name {
    color: var(--sky); font-weight: 600; font-size: 25px; letter-spacing: 1px; line-height: 1;
  }
  .contact__role { font-size: 17px; margin: 4px 0 12px; }
  .contact__list { list-style: none; }
  .contact__item {
    display: flex; align-items: center; gap: 10px; font-size: 18px; line-height: 30px;
  }
  .contact__item svg { width: 17px; height: 17px; flex: none; }
</style>
</head>
<body>
<main class="canvas">
  <section class="card card--front">
    <div class="brand-dot"></div>
    <div class="brand-name">TIDE HARBOR</div>
  </section>

  <section class="card card--back">
    <div class="side-band">
      <div class="brand-vertical">TIDE HARBOR</div>
      <div class="brand-dot"></div>
    </div>
    <div class="accent-stripe"></div>
    <div class="contact">
      <div class="contact__name">MARCUS ELLERY</div>
      <div class="contact__role">Managing Broker</div>
      <ul class="contact__list">
        <li class="contact__item">
          <svg viewBox="0 0 20 20" fill="none" stroke="#45a9cf" stroke-width="1.6"><circle cx="10" cy="10" r="8.5"/><path d="M7 6l1.5 2.5-1 1a6 6 0 0 0 3 3l1-1L14 13l-1 1.5c-3 0-7-4-7-7z"/></svg>
          (555) 014-2290
        </li>
        <li class="contact__item">
          <svg viewBox="0 0 20 20" fill="none" stroke="#45a9cf" stroke-width="1.6"><rect x="2" y="4.5" width="16" height="11"/><path d="M2 4.5l8 6 8-6"/></svg>
          info@tideharbor.com
        </li>
        <li class="contact__item">
          <svg viewBox="0 0 20 20" fill="none" stroke="#45a9cf" stroke-width="1.6"><circle cx="10" cy="10" r="8"/><ellipse cx="10" cy="10" rx="3.5" ry="8"/><path d="M2 10h16M3.5 6h13M3.5 14h13"/></svg>
          www.tideharbor.com
        </li>
      </ul>
    </div>
  </section>
</main>
</body>
</html>
```